New Business Card Design Project

I would like my card design to look exactly like the logo, design, layout, and print of the current attached file. The only change I would like made would be for the print to say THE KMW GROUP instead of THE HALLORAN GROUP. Basically, just replace his group name with my group name. I would also like the backgroud to be the same texture and color as the attached file. I love the dark blue lettering and house logo on the card.

I am completely open to the rest of the card design. I just want something clean and simple. Only basic contact info required on the card. Maybe just name: Kyle M Warrick and cell # 555.914.2087 and email kyle@orchidhomesagent.com

```html
<!DOCTYPE html>
<html lang="en">
<head>
<meta charset="utf-8">
<title>The KMW Group – Business Card</title>
<link rel="stylesheet" href="https://fonts.googleapis.com/css2?family=Lato:wght@400&display=swap">
<style>
  :root {
    --page: #ffffff;
    --card: #f5f5f3;
    --navy: #23265a;
    --ink: #1c1d33;
  }
  html, body {
    margin: 0;
    padding: 0;
    width: 1200px;
    height: 1200px;
    overflow: hidden;
    background: var(--page);
  }
  .card {
    position: absolute;
    left: 76px;
    top: 266px;
    width: 1040px;
    height: 652px;
    background: var(--card);
    font-family: "Lato", sans-serif;
    font-weight: 400;
  }
  .brand-square {
    position: absolute;
    left: 150px;
    top: 524px;
    width: 122px;
    height: 122px;
    background: var(--navy);
  }
  .brand-name {
    position: absolute;
    left: 318px;
    top: 530px;
    margin: 0;
    font-family: "Lato", sans-serif;
    font-weight: 400;
    font-size: 39px;
    line-height: 37px;
    letter-spacing: 3px;
    color: var(--navy);
  }
  .brand-name span { display: block; }
  .holder-name {
    position: absolute;
    left: 566px;
    top: 488px;
    margin: 0;
    font-family: "Lato", sans-serif;
    font-weight: 400;
    font-size: 61px;
    line-height: 70px;
    color: var(--navy);
    white-space: nowrap;
  }
  .contact {
    position: absolute;
    left: 566px;
    top: 585px;
    margin: 0;
    font-family: "Lato", sans-serif;
    font-size: 36px;
    line-height: 58px;
    color: var(--ink);
  }
  .contact-row { display: flex; white-space: nowrap; }
  .contact-label { width: 122px; }
  .contact-value { color: var(--navy); }
</style>
</head>
<body>
  <div class="card" style="left:0;top:0;width:0;height:0;background:none;"></div>
  <div class="brand-square" aria-hidden="true"></div>
  <p class="brand-name"><span>THE</span><span>KMW</span><span>GROUP</span></p>
  <h1 class="holder-name">Kyle M Warrick</h1>
  <div class="contact">
    <div class="contact-row"><span class="contact-label">Cell:</span><span class="contact-value">555.914.2087</span></div>
    <div class="contact-row"><span class="contact-label">Mail:</span><span class="contact-value">kyle@orchidhomesagent.com</span></div>
  </div>
</body>
</html>
```